Design "CLIFFROAMER" Shopify online store for hunting, outdoor and tactical accessories, appare

Design and setup Shopify platform online store for hunting, outdoor and tactical accessories, apparel.

Logo has been uploaded. Instagram, Facebook and domain all setuop

A really modern easy to navigate online store that I can add and remove categories, add and remove products, update images, slider images, must have a AUD, USD, EUR, NZD and GBP currency converter drop down. RRPs will start in AUD. domain name is already registered and logo is done. Products are being photographed in readiness for you to set up the site. Fast shopping cart as guest with just name and address vs joining and collecting info for newsletters. Ability to send out newsletters. Home page that showcases 4-6 key categories of the site with hero images that can be updated by me. A clear navigation pane across the top. In the shopping part a clear categories navigation that can be updated as required. Free postage Australia and NZ, international shipment extra. Ultimately I need a great design as we have great products appealing to hunters, people who love the outdoors from camping to hiking, to tactical supplies. It's important to be strong website that shows quality and is easy to get arouund. Most of all it is brand new so whatever you can do to help drive traffic to it please do so. I will be managing it when ready with view to hiring a social media/web analyst to support me in a month.

Target Market(s)

Australian hunters and outdoor lovers - camping, hiking, motorbikes (dirt bikes / MX), and tactical professionals

Industry/Entity Type

Online Shopping

Coding

Coded - Design and coding required

Number of Pages Required

5+ page

Requirements
Must have
• As per my description plus up to the designers. You are the experts. I want it to look great but ultimately it has to get traffic and SELL PRODUCT
• Would like option for people to review products, eg leave 1-5 stars.
• After pay and Paypal for payment is my suggestion but I'm not the expert
• Work on computers, tablets and smartphones - compatible for all devices
Nice to have
• Product thumbnails, rankings. Can click on product to see more pictures, video and details. Size charts for apparel.
• Products will be things such as bags, equipment, accessories, clothing - all designed for outdoor activities predominantly hunting, camping, MX dirt bike riding, fishing, etc

```html
<!DOCTYPE html>
<html lang="en">
<head>
<meta charset="utf-8">
<title>CLIFFROAMER — Hunting, Outdoor &amp; Tactical Store</title>
<link href="https://fonts.googleapis.com/css2?family=Oswald:wght@400;500;600;700&family=Open+Sans:wght@400;600;700&display=swap" rel="stylesheet">
<style>
:root{
  --orange:#f26522;
  --orange-dark:#d8521a;
  --black:#111111;
  --ink:#222222;
  --muted:#777777;
  --line:#e3e3e3;
  --peach:#f3c9a2;
  --mint:#b9d8cb;
  --grey-band:#ececec;
  --star:#f5b300;
  --white:#ffffff;
}
*{box-sizing:border-box;margin:0;padding:0}
html,body{width:1200px;height:5248px;overflow:hidden;background:var(--white)}
body{font-family:"Open Sans",Arial,sans-serif;color:var(--ink);font-size:15px}
a{color:inherit;text-decoration:none}
.wrap{width:1124px;margin:0 auto;position:relative}
svg{display:block}

.topbar{height:49px;background:var(--black);color:#fff;display:flex;justify-content:center;align-items:center;gap:34px;font-size:14px;font-weight:600}
.topbar span{display:flex;align-items:center;gap:8px}

.header{height:161px}
.header .wrap{height:161px;display:flex;align-items:center}
.logo{font-family:"Oswald",Arial,sans-serif;font-weight:700;font-size:44px;letter-spacing:1px;color:var(--ink);display:flex;align-items:center;gap:14px}
.logo .mark{width:22px;height:22px;background:var(--orange)}
.header-right{margin-left:auto;display:flex;align-items:center;gap:34px}
.call{display:flex;align-items:center;gap:16px}
.call .circle{width:64px;height:64px;border:2px solid var(--line);border-radius:50%;display:flex;align-items:center;justify-content:center}
.call .txt{font-size:15px;line-height:22px;color:#444}
.cart{position:relative}
.cart .badge{position:absolute;top:-10px;right:-12px;width:22px;height:22px;border-radius:50%;background:#888;color:#fff;font-size:11px;display:flex;align-items:center;justify-content:center}
.currency{display:flex;align-items:center;gap:8px}
.flag{width:38px;height:24px;background:linear-gradient(#b22234 0 14%,#fff 14% 28%,#b22234 28% 42%,#fff 42% 57%,#b22234 57% 71%,#fff 71% 85%,#b22234 85%);position:relative}
.flag:after{content:"";position:absolute;left:0;top:0;width:16px;height:13px;background:#3c3b6e}

.navbar{height:70px;background:var(--orange)}
.navbar .wrap{height:70px;display:flex;align-items:center}
.search{margin-left:auto;width:420px;height:44px;background:#fff;display:flex;align-items:center;padding:0 18px;font-size:14px;color:#888;justify-content:space-between}

.features{height:186px;border-bottom:1px solid var(--line)}
.features .wrap{display:flex;gap:40px;padding-top:34px}
.feature{flex:1;display:flex;gap:16px}
.feature h4{font-size:15px;font-weight:600;text-transform:uppercase;color:#333;margin-bottom:8px}
.feature p{font-size:15px;color:#777;line-height:24px}

.catbar{height:59px;background:var(--black);color:#fff}
.catbar .wrap{height:59px;display:flex;align-items:center;justify-content:space-between;font-weight:700;font-size:18px;text-transform:uppercase}

.hero{height:333px;position:relative;background:linear-gradient(180deg,#1a1310 0%,#3a1b0d 45%,#c9460e 78%,#f07a1e 88%,#1a0d07 100%);display:flex;flex-direction:column;align-items:center;justify-content:center;color:#fff}
.hero h1{font-family:"Oswald",Arial,sans-serif;font-size:52px;letter-spacing:6px;font-weight:600}
.hero p{font-size:16px;margin:6px 0 24px}
.btn{display:inline-flex;align-items:center;justify-content:center;background:var(--orange);color:#fff;font-weight:600;text-transform:uppercase}
.hero .btn{width:190px;height:54px;font-size:18px;font-family:"Oswald",Arial,sans-serif}
.arrow-circle{position:absolute;top:152px;width:34px;height:34px;border-radius:50%;background:rgba(0,0,0,.5);display:flex;align-items:center;justify-content:center}

.promos{height:237px;padding-top:17px}
.promos .wrap{display:flex;gap:14px}
.promo{flex:1;height:220px;display:flex;align-items:center;padding:0 22px;gap:14px}
.promo .copy{flex:1}
.promo h5{font-size:18px;font-weight:600;text-transform:uppercase;line-height:26px;color:#333}
.promo h5 em{font-style:normal;color:var(--orange)}
.promo .btn{width:132px;height:44px;font-size:16px;margin-top:16px;font-family:"Oswald",Arial,sans-serif}
.promo .pic{width:120px;height:130px;border-radius:4px}
.promo.peach{background:var(--peach)}
.promo.mint{background:var(--mint)}

.sec-head{height:88px;position:relative;display:flex;align-items:center}
.sec-head .tab{height:84px;padding:0 80px 0 26px;background:var(--orange);color:#fff;font-family:"Oswald",Arial,sans-serif;font-size:28px;font-weight:600;text-transform:uppercase;display:flex;align-items:center;clip-path:polygon(0 0,82% 0,100% 100%,0 100%)}
.sec-head:after{content:"";position:absolute;left:0;right:0;bottom:2px;height:3px;background:var(--orange)}
.sec-head .nav{margin-left:auto;display:flex;gap:10px}
.sec-head .nav span{width:34px;height:34px;border-radius:50%;border:1px solid #ccc;display:flex;align-items:center;justify-content:center}

.products{display:flex;gap:30px;padding-top:21px}
.product{width:355px;text-align:center}
.product .img{height:388px;border:1px solid var(--line);display:flex;align-items:center;justify-content:center}
.product .img div{width:240px;height:200px;border-radius:6px}
.product h3{font-family:"Oswald",Arial,sans-serif;font-weight:400;font-size:23px;text-transform:uppercase;margin-top:38px}
.price{display:flex;justify-content:center;align-items:center;gap:10px;margin-top:12px;color:var(--orange);font-size:20px}
.addcart{margin-top:14px;display:inline-flex;height:57px;font-family:"Oswald",Arial,sans-serif;font-size:18px}
.addcart .ic{width:50px;background:var(--orange-dark);display:flex;align-items:center;justify-content:center}
.addcart .lbl{width:150px;background:var(--orange);color:#fff;display:flex;align-items:center;justify-content:center;text-transform:uppercase}

.mosaic{height:456px;margin-top:27px;display:grid;grid-template-columns:298px 500px 296px;gap:15px}
.tile{position:relative}
.tile .lbl{position:absolute;left:0;right:0;height:40px;background:rgba(242,101,34,.9);color:#fff;font-family:"Oswald",Arial,sans-serif;text-transform:uppercase;display:flex;align-items:center;justify-content:center;font-size:17px}
.tile.big .lbl{height:62px;font-size:24px}
.stack{display:grid;grid-template-rows:1fr 1fr;gap:10px}

.blog{display:flex;gap:30px;padding-top:18px}
.post{width:355px}
.post .img{height:343px;position:relative}
.post .date{position:absolute;right:0;bottom:0;width:88px;height:122px;background:var(--orange);color:#fff;font-family:"Oswald",Arial,sans-serif;font-size:20px;display:flex;flex-direction:column;align-items:center;justify-content:center;line-height:30px;font-weight:500}
.post h3{font-family:"Oswald",Arial,sans-serif;font-weight:500;font-size:20px;text-transform:uppercase;margin-top:36px}
.post p{font-size:15px;color:#777;line-height:30px;margin-top:10px}

.brands{height:200px;display:flex;align-items:center;justify-content:space-around;padding-top:10px}
.brand{font-family:"Oswald",Arial,sans-serif;font-weight:700;font-size:62px;color:#3a3a3a;letter-spacing:1px}
.brand.light{color:#9a9a9a}

.newsletter{height:210px;background:var(--grey-band);margin-top:60px}
.newsletter .wrap{height:210px;display:flex;align-items:center}
.newsletter h4{font-family:"Oswald",Arial,sans-serif;font-weight:500;font-size:28px;text-transform:uppercase;display:flex;align-items:center;gap:18px}
.newsletter form{margin-left:auto;display:flex}
.newsletter .field{width:514px;height:76px;background:#fff;display:flex;align-items:center;padding:0 22px;color:#888}
.newsletter .sub{width:216px;height:76px;background:var(--black);color:#fff;font-family:"Oswald",Arial,sans-serif;font-size:22px;display:flex;align-items:center;justify-content:center;font-weight:600}

.footer{height:886px;background:var(--black);color:#fff}
.footer .wrap{padding-top:80px;height:886px;position:relative}
.f-logo{font-family:"Oswald",Arial,sans-serif;font-weight:700;font-size:40px;display:flex;align-items:center;gap:12px}
.f-logo .mark{width:20px;height:20px;background:var(--orange)}
.contact{margin-top:46px;font-size:18px;line-height:30px}
.contact div{display:flex;gap:20px;margin-bottom:22px;width:450px}
.social{display:flex;gap:14px;margin-top:16px}
.social span{width:50px;height:50px;border-radius:50%;border:2px solid #fff}
.col{position:absolute}
.col h5{font-family:"Oswald",Arial,sans-serif;font-size:28px;font-weight:500;text-transform:uppercase;margin-bottom:30px}
.col ul{list-style:none;font-size:18px}
.col li{height:66px;display:flex;align-items:center;gap:26px}
.col li:before{content:"»";font-size:18px}
.links{display:grid}
.copyright{height:120px;background:var(--black);border-top:1px solid #333;color:#fff}
.copyright .wrap{height:120px;display:flex;align-items:center;font-size:17px}
.cards{margin-left:auto;display:flex;gap:8px}
.cards span{width:58px;height:36px;border-radius:4px;background:#dcdcdc}
</style>
</head>
<body>

<div class="topbar">
  <span><svg width="14" height="16" viewBox="0 0 14 16"><rect x="1" y="7" width="12" height="9" fill="#fff"/><path d="M4 7V4a3 3 0 016 0v3" stroke="#fff" stroke-width="2" fill="none"/></svg>Log in</span>
  <span><svg width="16" height="16" viewBox="0 0 16 16"><path d="M2 14l2-5 8-8 3 3-8 8z" fill="#fff"/></svg>Register</span>
  <span><svg width="16" height="14" viewBox="0 0 16 14"><path d="M8 14L1 7a4 4 0 017-5 4 4 0 017 5z" fill="#fff"/></svg>My Wishlist</span>
  <span><svg width="14" height="16" viewBox="0 0 14 16"><circle cx="7" cy="4" r="4" fill="#fff"/><path d="M0 16a7 7 0 0114 0z" fill="#fff"/></svg>My Account</span>
</div>

<header class="header">
  <div class="wrap">
    <a class="logo"><span class="mark"></span>CLIFFROAMER</a>
    <div class="header-right">
      <div class="call">
        <div class="circle"><svg width="26" height="26" viewBox="0 0 24 24"><path d="M6.6 10.8a15 15 0 006.6 6.6l2.2-2.2c.3-.3.7-.4 1-.2 1.1.4 2.3.6 3.6.6.6 0 1 .4 1 1V20c0 .6-.4 1-1 1A17 17 0 013 4c0-.6.4-1 1-1h3.5c.6 0 1 .4 1 1 0 1.3.2 2.5.6 3.6.1.3 0 .7-.2 1z" fill="var(--orange)"/></svg></div>
        <div class="txt">CALL US HERE<br>(555)-010-2231</div>
      </div>
      <div class="cart"><svg width="44" height="40" viewBox="0 0 44 40"><path d="M2 4h7l6 22h22l5-16H12" stroke="var(--orange)" stroke-width="3.5" fill="none"/><circle cx="17" cy="34" r="3.5" fill="var(--orange)"/><circle cx="34" cy="34" r="3.5" fill="var(--orange)"/></svg><span class="badge">0</span></div>
      <div class="currency"><span class="flag"></span><svg width="10" height="6" viewBox="0 0 10 6"><path d="M0 0h10L5 6z" fill="#333"/></svg></div>
    </div>
  </div>
</header>

<nav class="navbar">
  <div class="wrap">
    <svg width="32" height="24" viewBox="0 0 32 24"><rect width="32" height="4" fill="#fff"/><rect y="10" width="32" height="4" fill="#fff"/><rect y="20" width="32" height="4" fill="#fff"/></svg>
    <div class="search">SEARCH...<svg width="18" height="18" viewBox="0 0 18 18"><circle cx="7.5" cy="7.5" r="6" stroke="#333" stroke-width="2.5" fill="none"/><path d="M12 12l5 5" stroke="#333" stroke-width="2.5"/></svg></div>
  </div>
</nav>

<section class="features">
  <div class="wrap">
    <div class="feature">
      <svg width="34" height="34" viewBox="0 0 34 34"><rect x="3" y="13" width="28" height="19" fill="var(--orange)"/><rect x="1" y="8" width="32" height="7" fill="var(--orange-dark)"/><rect x="15" y="8" width="4" height="24" fill="#fff"/><path d="M17 8c-4-8-11-6-9-1M17 8c4-8 11-6 9-1" stroke="var(--orange)" stroke-width="2.5" fill="none"/></svg>
      <div><h4>Free postage Australia and NZ</h4><p>Quis nostrud exercitation ullamco laboris nisi uto consequa.</p></div>
    </div>
    <div class="feature">
      <svg width="38" height="30" viewBox="0 0 38 30"><rect x="0" y="3" width="24" height="19" fill="var(--orange)"/><path d="M24 9h8l6 7v6H24z" fill="var(--orange)"/><circle cx="8" cy="25" r="4" fill="var(--orange-dark)"/><circle cx="30" cy="25" r="4" fill="var(--orange-dark)"/></svg>
      <div><h4>International shipment extra</h4><p>Quis nostrud exercitation ullamco laboris nisi uto consequa.</p></div>
    </div>
    <div class="feature">
      <svg width="34" height="34" viewBox="0 0 34 34"><rect x="2" y="5" width="30" height="27" fill="none" stroke="var(--orange)" stroke-width="3"/><rect x="2" y="5" width="30" height="8" fill="var(--orange)"/><rect x="8" y="1" width="4" height="8" fill="var(--orange)"/><rect x="22" y="1" width="4" height="8" fill="var(--orange)"/><g fill="var(--orange)"><rect x="8" y="17" width="4" height="4"/><rect x="15" y="17" width="4" height="4"/><rect x="22" y="17" width="4" height="4"/><rect x="8" y="24" width="4" height="4"/><rect x="15" y="24" width="4" height="4"/></g></svg>
      <div><h4>Delivery schedule</h4><p>Quis nostrud exercitation ullamco laboris nisi uto consequa.</p></div>
    </div>
  </div>
</section>

<div class="catbar">
  <div class="wrap">Categories<svg width="26" height="20" viewBox="0 0 26 20"><g fill="#fff"><rect width="4" height="4"/><rect x="7" width="19" height="4"/><rect y="8" width="4" height="4"/><rect x="7" y="8" width="19" height="4"/><rect y="16" width="4" height="4"/><rect x="7" y="16" width="19" height="4"/></g></svg></div>
</div>

<section class="hero" role="img" aria-label="Hunter in camouflage silhouetted against an orange sunset over the bush">
  <span class="arrow-circle" style="left:48px"><svg width="10" height="14" viewBox="0 0 10 14"><path d="M8 1L2 7l6 6" stroke="#fff" stroke-width="2.5" fill="none"/></svg></span>
  <h1>CLIFFROAMER</h1>
  <p>Excepteur sint occaecat cupidatat non proident</p>
  <a class="btn">Shop Now</a>
  <span class="arrow-circle" style="right:48px"><svg width="10" height="14" viewBox="0 0 10 14"><path d="M2 1l6 6-6 6" stroke="#fff" stroke-width="2.5" fill="none"/></svg></span>
</section>

<section class="promos">
  <div class="wrap">
    <div class="promo peach">
      <div class="pic" role="img" aria-label="Brown leather bag" style="background:linear-gradient(135deg,#8a5a34,#4a2c17)"></div>
      <div class="copy"><h5>Large collection of <em>clothing...</em></h5><a class="btn">Shop Now</a></div>
    </div>
    <div class="promo mint">
      <div class="copy"><h5>Buy online <em>the best bags...</em></h5><a class="btn">Shop Now</a></div>
      <div class="pic" role="img" aria-label="Camouflage field jacket" style="background:linear-gradient(135deg,#5d6b3c,#2f3a20)"></div>
    </div>
    <div class="promo peach">
      <div class="copy"><h5>Everyday lowest prices <em>predominantly hunting</em></h5><a class="btn">Shop Now</a></div>
      <div class="pic" role="img" aria-label="Hunting rifles" style="background:linear-gradient(135deg,#6d4a2e,#2a2a2a)"></div>
    </div>
  </div>
</section>

<svg width="0" height="0" style="position:absolute"><defs><path id="s" d="M8 0l2.4 5 5.4.6-4 3.7 1.1 5.4L8 12l-4.9 2.7 1.1-5.4-4-3.7 5.4-.6z"/></defs></svg>

<main class="wrap">
  <div class="sec-head"><div class="tab">Featured Products</div><div class="nav"><span><svg width="8" height="12" viewBox="0 0 8 12"><path d="M6 1L1 6l5 5" stroke="#333" stroke-width="2" fill="none"/></svg></span><span><svg width="8" height="12" viewBox="0 0 8 12"><path d="M2 1l5 5-5 5" stroke="#333" stroke-width="2" fill="none"/></svg></span></div></div>

  <div class="products">
    <div class="product"><div class="img"><div role="img" aria-label="Black handgun replica" style="background:linear-gradient(135deg,#6a6a6a,#1e1e1e)"></div></div><h3>Ullamco Laborinisi</h3>
      <div class="price">$56.98<svg width="90" height="16" viewBox="0 0 90 16"><g fill="var(--star)"><use href="#s"/><use href="#s" x="18"/><use href="#s" x="36"/><use href="#s" x="54"/><use href="#s" x="72"/></g></svg></div>
      <a class="addcart"><span class="ic"><svg width="20" height="18" viewBox="0 0 20 18"><path d="M0 1h4l3 10h10l3-7H5" stroke="#fff" stroke-width="2" fill="none"/><circle cx="8" cy="15" r="2" fill="#fff"/><circle cx="16" cy="15" r="2" fill="#fff"/></svg></span><span class="lbl">Add to cart</span></a></div>
    <div class="product"><div class="img"><div role="img" aria-label="Orange and grey dome tent" style="background:linear-gradient(135deg,#f0a830,#7a7a7a)"></div></div><h3>Sed Quia Consequ</h3>
      <div class="price">$56.98<svg width="90" height="16" viewBox="0 0 90 16"><g fill="var(--star)"><use href="#s"/><use href="#s" x="18"/><use href="#s" x="36"/><use href="#s" x="54"/><use href="#s" x="72"/></g></svg></div>
      <a class="addcart"><span class="ic"><svg width="20" height="18" viewBox="0 0 20 18"><path d="M0 1h4l3 10h10l3-7H5" stroke="#fff" stroke-width="2" fill="none"/><circle cx="8" cy="15" r="2" fill="#fff"/><circle cx="16" cy="15" r="2" fill="#fff"/></svg></span><span class="lbl">Add to cart</span></a></div>
    <div class="product"><div class="img"><div role="img" aria-label="Yellow hiking backpack" style="background:linear-gradient(135deg,#f5c518,#3a3a3a)"></div></div><h3>Reprehenderit Qui</h3>
      <div class="price">$56.98<svg width="90" height="16" viewBox="0 0 90 16"><g fill="var(--star)"><use href="#s"/><use href="#s" x="18"/><use href="#s" x="36"/><use href="#s" x="54"/><use href="#s" x="72"/></g></svg></div>
      <a class="addcart"><span class="ic"><svg width="20" height="18" viewBox="0 0 20 18"><path d="M0 1h4l3 10h10l3-7H5" stroke="#fff" stroke-width="2" fill="none"/><circle cx="8" cy="15" r="2" fill="#fff"/><circle cx="16" cy="15" r="2" fill="#fff"/></svg></span><span class="lbl">Add to cart</span></a></div>
  </div>

  <div class="mosaic">
    <div class="stack">
      <div class="tile" role="img" aria-label="Hunting in the bush" style="background:linear-gradient(160deg,#7b8a5a,#3c3a2a)"><span class="lbl" style="top:84px">Predominantly Hunting</span></div>
      <div class="tile" role="img" aria-label="Motocross dirt bike rider" style="background:linear-gradient(160deg,#6f95c8,#8a7550)"><span class="lbl" style="top:84px">MX Dirt Bike Riding</span></div>
    </div>
    <div class="tile big" role="img" aria-label="Hunting horn on a grey backdrop" style="background:radial-gradient(circle at 50% 40%,#e6e6e6,#9a9a9a)"><span class="lbl" style="top:197px">Hunting Equipment</span></div>
    <div class="tile big" role="img" aria-label="Campfire at dusk" style="background:linear-gradient(180deg,#5a6a7a 0%,#3c4a3a 45%,#e0641a 75%,#3a2010 100%)"><span class="lbl" style="top:197px">Camping</span></div>
  </div>

  <div class="sec-head" style="margin-top:21px"><div class="tab">New Products</div><div class="nav"><span><svg width="8" height="12" viewBox="0 0 8 12"><path d="M6 1L1 6l5 5" stroke="#333" stroke-width="2" fill="none"/></svg></span><span><svg width="8" height="12" viewBox="0 0 8 12"><path d="M2 1l5 5-5 5" stroke="#333" stroke-width="2" fill="none"/></svg></span></div></div>

  <div class="products">
    <div class="product"><div class="img"><div role="img" aria-label="Blue trekking backpack" style="background:linear-gradient(135deg,#3a8de0,#1a2a4a)"></div></div><h3>Cillum Dolore Eu Fugi</h3>
      <div class="price">$56.98<svg width="90" height="16" viewBox="0 0 90 16"><g fill="var(--star)"><use href="#s"/><use href="#s" x="18"/><use href="#s" x="36"/><use href="#s" x="54"/><use href="#s" x="72"/></g></svg></div>
      <a class="addcart"><span class="ic"><svg width="20" height="18" viewBox="0 0 20 18"><path d="M0 1h4l3 10h10l3-7H5" stroke="#fff" stroke-width="2" fill="none"/><circle cx="8" cy="15" r="2" fill="#fff"/><circle cx="16" cy="15" r="2" fill="#fff"/></svg></span><span class="lbl">Add to cart</span></a></div>
    <div class="product"><div class="img"><div role="img" aria-label="Black iron fire pit with logs" style="background:linear-gradient(135deg,#6b4a30,#1e1e1e)"></div></div><h3>Excepteur Sint Occ</h3>
      <div class="price">$56.98<svg width="90" height="16" viewBox="0 0 90 16"><g fill="var(--star)"><use href="#s"/><use href="#s" x="18"/><use href="#s" x="36"/><use href="#s" x="54"/><use href="#s" x="72"/></g></svg></div>
      <a class="addcart"><span class="ic"><svg width="20" height="18" viewBox="0 0 20 18"><path d="M0 1h4l3 10h10l3-7H5" stroke="#fff" stroke-width="2" fill="none"/><circle cx="8" cy="15" r="2" fill="#fff"/><circle cx="16" cy="15" r="2" fill="#fff"/></svg></span><span class="lbl">Add to cart</span></a></div>
    <div class="product"><div class="img"><div role="img" aria-label="White enduro dirt bike" style="background:linear-gradient(135deg,#e8e8e8,#2a2a2a)"></div></div><h3>Dminima Veniam</h3>
      <div class="price">$56.98<svg width="90" height="16" viewBox="0 0 90 16"><g fill="var(--star)"><use href="#s"/><use href="#s" x="18"/><use href="#s" x="36"/><use href="#s" x="54"/><use href="#s" x="72"/></g></svg></div>
      <a class="addcart"><span class="ic"><svg width="20" height="18" viewBox="0 0 20 18"><path d="M0 1h4l3 10h10l3-7H5" stroke="#fff" stroke-width="2" fill="none"/><circle cx="8" cy="15" r="2" fill="#fff"/><circle cx="16" cy="15" r="2" fill="#fff"/></svg></span><span class="lbl">Add to cart</span></a></div>
  </div>

  <div class="sec-head" style="margin-top:31px"><div class="tab">Blog Posts</div><div class="nav"><span><svg width="8" height="12" viewBox="0 0 8 12"><path d="M6 1L1 6l5 5" stroke="#333" stroke-width="2" fill="none"/></svg></span><span><svg width="8" height="12" viewBox="0 0 8 12"><path d="M2 1l5 5-5 5" stroke="#333" stroke-width="2" fill="none"/></svg></span></div></div>

  <div class="blog">
    <div class="post"><div class="img" role="img" aria-label="Rifle resting on a dirt track" style="background:linear-gradient(150deg,#6a5a3a,#3a4a2a)"><span class="date">MAY<span>29,</span>2017</span></div>
      <h3>Asperatur aut odit aut fugit</h3><p>Sed ut perspiciatis unde omnis iste natus error sit voluptatem accusantium dolo-remque laudantium, totam.</p></div>
    <div class="post"><div class="img" role="img" aria-label="Silhouette at twilight under a blue sky" style="background:linear-gradient(180deg,#0f2a5a 0%,#27407a 55%,#e07a2a 82%,#111 100%)"><span class="date">MAY<span>29,</span>2017</span></div>
      <h3>Ut enim ad minima veniam</h3><p>Sed ut perspiciatis unde omnis iste natus error sit voluptatem accusantium dolorem-que laudantium, totam.</p></div>
    <div class="post"><div class="img" role="img" aria-label="Burrow entrance among mossy rocks" style="background:linear-gradient(150deg,#9aa090,#3a3a30)"><span class="date">MAY<span>29,</span>2017</span></div>
      <h3>Quis nostrum exercitationem</h3><p>Sed ut perspiciatis unde omnis iste natus error sit voluptatem accusantium dolorem-que laudantium, totam.</p></div>
  </div>

  <div class="sec-head" style="margin-top:42px"><div class="tab">Brands</div><div class="nav"><span><svg width="8" height="12" viewBox="0 0 8 12"><path d="M6 1L1 6l5 5" stroke="#333" stroke-width="2" fill="none"/></svg></span><span><svg width="8" height="12" viewBox="0 0 8 12"><path d="M2 1l5 5-5 5" stroke="#333" stroke-width="2" fill="none"/></svg></span></div></div>

  <div class="brands">
    <span class="brand">BRAXLEN</span>
    <span class="brand">KESTRAVO</span>
    <span class="brand light">TOLMERA</span>
  </div>
</main>

<section class="newsletter">
  <div class="wrap">
    <h4><svg width="50" height="44" viewBox="0 0 50 44"><path d="M2 18L25 2l23 16v24H2z" fill="var(--orange)"/><rect x="10" y="8" width="30" height="22" fill="#fff"/><path d="M2 18l23 15 23-15v24H2z" fill="var(--orange-dark)"/></svg>Sign up newsletter</h4>
    <form><span class="field">Enter Email..</span><span class="sub">SUBSCRIBE</span></form>
  </div>
</section>

<footer class="footer">
  <div class="wrap">
    <div class="f-logo"><span class="mark"></span>CLIFFROAMER</div>
    <div class="contact">
      <div><svg width="22" height="30" viewBox="0 0 22 30"><path d="M11 0a11 11 0 0111 11c0 8-11 19-11 19S0 19 0 11A11 11 0 0111 0z" fill="none" stroke="#fff" stroke-width="2.5"/><circle cx="11" cy="11" r="4" fill="#fff"/></svg><span>36RG, Sit voluptatem accusantium dolore laud rem aperiameaque ipsa.</span></div>
      <div><svg width="24" height="24" viewBox="0 0 24 24"><path d="M6.6 10.8a15 15 0 006.6 6.6l2.2-2.2c.3-.3.7-.4 1-.2 1.1.4 2.3.6 3.6.6.6 0 1 .4 1 1V20c0 .6-.4 1-1 1A17 17 0 013 4c0-.6.4-1 1-1h3.5c.6 0 1 .4 1 1 0 1.3.2 2.5.6 3.6.1.3 0 .7-.2 1z" fill="none" stroke="#fff" stroke-width="1.8"/></svg><span>Phone: (555) - 014 - 7720</span></div>
      <div><svg width="26" height="20" viewBox="0 0 26 20"><rect x="1" y="1" width="24" height="18" fill="none" stroke="#fff" stroke-width="2"/><path d="M1 1l12 10L25 1" stroke="#fff" stroke-width="2" fill="none"/></svg><span>Email : hello@cliffroamer.example</span></div>
    </div>
    <div class="social" aria-label="Social profiles"><span></span><span></span><span></span><span></span></div>

    <div class="col" style="left:550px;top:80px"><h5>Menus</h5><ul><li>Home</li><li>Hunting</li><li>Outdoor</li><li>Tactical accessories</li><li>Apparel</li></ul></div>
    <div class="col" style="left:890px;top:80px"><h5>My Account</h5><ul><li>Policies</li><li>Orders</li><li>Return</li><li>Bulk Discount</li><li>Quality</li></ul></div>

    <div class="col" style="left:0;top:568px"><h5>Quick Links</h5>
      <ul class="links" style="grid-template-columns:200px 200px"><li>Press</li><li>Employment</li><li>Wholesale</li><li>Size Chart</li><li>Policies</li></ul></div>
    <div class="col" style="left:455px;top:568px"><h5>Other Links</h5>
      <ul class="links" style="grid-template-columns:322px 300px"><li>Request Quote</li><li>Terms of Use</li><li>Information</li><li>Knowledge</li><li>Phone &amp; Mail Privacy</li></ul></div>
  </div>
</footer>

<div class="copyright">
  <div class="wrap">© copyright 2017 CLIFFROAMER . All Rights Reserved
    <div class="cards" aria-label="Accepted payment methods"><span></span><span></span><span></span><span></span><span></span></div>
  </div>
</div>

</body>
</html>
```